Bref créative
Business Cards and Letterhead
85 mm x 55 mm / DIN A4 210 mm × 297 mm
Professional
Dominik R. Hartl
Lindenweg 7, 14471 Potsdam
info@lbr-planung.example
www.lbr-planung.example
Please use the standard german sizes for business cards and letters:
85 mm x 55 mm
DIN A4: 210 mm × 297 mm

```html
<!DOCTYPE html>
<html lang="de">
<head>
<meta charset="utf-8">
<title>LBR Planung – Visitenkarte</title>
<link rel="stylesheet" href="https://fonts.googleapis.com/css2?family=Open+Sans:wght@400;600;700&display=swap">
<style>
  :root {
    --bg: #e6e6e6;
    --card-white: #ffffff;
    --orange: #f39a2e;
    --orange-dark: #e9851a;
    --swoosh-grey: #a9a9a9;
    --ink: #333333;
    --text-light: #ffffff;
  }
  html, body {
    margin: 0;
    padding: 0;
    width: 1200px;
    height: 1018px;
    overflow: hidden;
    background: var(--bg);
    font-family: "Open Sans", Arial, sans-serif;
  }
  .business-card {
    position: absolute;
    left: 100px;
    top: 185px;
    width: 1000px;
    height: 647px;
    border-radius: 28px;
    overflow: hidden;
    background: var(--card-white);
    box-shadow: 0 10px 30px rgba(0,0,0,0.18);
  }
  .card-shapes {
    position: absolute;
    inset: 0;
  }
  .brand {
    position: absolute;
    left: 60px;
    top: 70px;
  }
  .brand-name {
    display: flex;
    align-items: center;
    gap: 18px;
    font-size: 78px;
    font-weight: 700;
    color: var(--ink);
    line-height: 1;
    letter-spacing: -1px;
  }
  .brand-mark {
    width: 44px;
    height: 44px;
    background: var(--orange);
  }
  .brand-tagline {
    margin-top: 10px;
    font-size: 19px;
    font-weight: 600;
    color: var(--ink);
    letter-spacing: 0.2px;
  }
  .holder-name {
    position: absolute;
    left: 60px;
    top: 462px;
    margin: 0;
    font-size: 44px;
    font-weight: 600;
    color: var(--text-light);
  }
  .contact-divider {
    position: absolute;
    left: 560px;
    top: 375px;
    width: 2px;
    height: 235px;
    background: rgba(255,255,255,0.85);
  }
  .contact-list {
    position: absolute;
    left: 585px;
    top: 370px;
    margin: 0;
    padding: 0;
    list-style: none;
    color: var(--text-light);
    font-size: 21px;
    line-height: 39px;
  }
  .contact-list li {
    display: flex;
    align-items: center;
    gap: 14px;
  }
  .contact-icon {
    width: 20px;
    height: 20px;
    flex: none;
  }
</style>
</head>
<body>
  <article class="business-card">
    <svg class="card-shapes" viewBox="0 0 1000 647" width="1000" height="647" aria-hidden="true">
      <path d="M0,300 C260,330 560,300 1000,150 L1000,270 C640,360 300,350 0,330 Z" fill="var(--swoosh-grey)"/>
      <path d="M0,335 C300,360 640,370 1000,275 L1000,647 L0,647 Z" fill="var(--orange)"/>
      <path d="M0,335 C300,360 640,370 1000,275 L1000,290 C640,385 300,372 0,348 Z" fill="var(--orange-dark)"/>
    </svg>

    <header class="brand">
      <div class="brand-name"><span>lbrplanung</span><span class="brand-mark"></span></div>
      <div class="brand-tagline">Unternehmensberatung · Coaching · Seminare</div>
    </header>

    <h1 class="holder-name">Dominik R. Hartl</h1>
    <div class="contact-divider"></div>

    <ul class="contact-list">
      <li>
        <svg class="contact-icon" viewBox="0 0 20 20" aria-hidden="true"><path d="M10 2 L19 10 H16 V18 H12 V13 H8 V18 H4 V10 H1 Z" fill="#fff"/></svg>
        Lindenweg 7, 14471 Potsdam
      </li>
      <li>
        <svg class="contact-icon" viewBox="0 0 20 20" aria-hidden="true"><path d="M5 2 L8 2 L9 6 L7 8 C8 11 9 12 12 13 L14 11 L18 12 L18 15 C18 17 16 18 14 18 C8 17 3 12 2 6 C2 4 3 2 5 2 Z" fill="#fff"/></svg>
        (0331) 555 01 20-0
      </li>
      <li>
        <svg class="contact-icon" viewBox="0 0 20 20" aria-hidden="true"><rect x="5" y="1" width="10" height="18" rx="2" fill="#fff"/><rect x="7" y="3" width="6" height="11" fill="var(--orange)"/></svg>
        (0170) 555 01 07
      </li>
      <li>
        <svg class="contact-icon" viewBox="0 0 20 20" aria-hidden="true"><rect x="2" y="8" width="16" height="10" rx="1" fill="#fff"/><rect x="5" y="2" width="10" height="7" fill="#fff"/><rect x="6" y="11" width="8" height="2" fill="var(--orange)"/></svg>
        (0331) 555 01 20-9
      </li>
      <li>
        <svg class="contact-icon" viewBox="0 0 20 20" aria-hidden="true"><rect x="1" y="4" width="18" height="12" rx="1" fill="#fff"/><path d="M1 5 L10 11 L19 5" fill="none" stroke="var(--orange)" stroke-width="1.5"/></svg>
        info@lbr-planung.example
      </li>
      <li>
        <svg class="contact-icon" viewBox="0 0 20 20" aria-hidden="true"><circle cx="10" cy="10" r="8" fill="none" stroke="#fff" stroke-width="2"/><path d="M2 10 H18 M10 2 C6 6 6 14 10 18 C14 14 14 6 10 2" fill="none" stroke="#fff" stroke-width="1.5"/></svg>
        www.lbr-planung.example
      </li>
    </ul>
  </article>
</body>
</html>
```